KWT BUSINESS CARD

I'd like a new business card for the folks in my office. I recently became aware of a company that produces extra thick cards that seem to me to make excellent use of embossing. I have a logo that I like so I just need a design that uses embossing effectively, is simple and uses minimal color.

I am uploading our current logo of a tooth with a brush above it. I am also uploading another file with the words of our business. In your design please use the square version of the tooth vs. the strectched version. The original logo is the more square image but please use the words and the fonts of "Wexmoor Dental Group" and incorporate that in the design.

Industry/Entity Type

Business

Colors
ffffff

Requirements
Must have
• Logo, company name (also a part of our existing logo), employee name and title, phone number and website address. Must be simple
Nice to have
• Embossed - Maybe a solid color on the back
Should not have
• Must not be too complex or busy

```html
<!DOCTYPE html>
<html lang="en">
<head>
<meta charset="utf-8">
<title>KWT Business Card</title>
<link rel="stylesheet" href="https://fonts.googleapis.com/css2?family=Questrial&display=swap">
<style>
  :root {
    --backdrop: #e9e6e1;
    --card-white: #ffffff;
    --brand-blue: #3f4598;
    --brand-green: #14ab4b;
    --frame-blue: #3a5ea8;
    --ink: #1a1a1a;
    --card-shadow: rgba(0, 0, 0, 0.18);
  }
  * { box-sizing: border-box; margin: 0; padding: 0; }
  html, body {
    width: 1200px;
    height: 784px;
    overflow: hidden;
    background: var(--backdrop);
    font-family: "Questrial", "Century Gothic", sans-serif;
  }
  .stage {
    width: 1200px;
    height: 784px;
    display: flex;
    align-items: center;
    justify-content: center;
    gap: 40px;
  }
  .card {
    position: relative;
    width: 560px;
    height: 320px;
    overflow: hidden;
    box-shadow: 0 6px 18px var(--card-shadow);
  }

  /* Back side */
  .card-back { background: var(--brand-green); }
  .card-back .band-top {
    position: absolute;
    left: 0; top: 0;
    width: 100%;
    height: 48%;
    background: var(--brand-blue);
  }
  .card-back .back-name {
    position: absolute;
    inset: 0;
    display: flex;
    align-items: center;
    justify-content: center;
    color: var(--card-white);
    font-size: 64px;
    letter-spacing: 6px;
  }

  /* Front side */
  .card-front { background: var(--card-white); }
  .card-front .frame {
    position: absolute;
    left: 18px; top: 16px; right: 16px; bottom: 18px;
    border-top: 3px solid var(--frame-blue);
    border-right: 3px solid var(--frame-blue);
    border-bottom: 3px solid var(--brand-green);
    border-left: 3px solid var(--brand-green);
  }
  .brand {
    position: absolute;
    left: 44px; top: 40px;
    display: flex;
    align-items: center;
    gap: 16px;
  }
  .brand-square {
    width: 96px;
    height: 96px;
    background: linear-gradient(var(--brand-blue) 0 50%, var(--brand-green) 50% 100%);
  }
  .brand-name {
    color: var(--ink);
    font-size: 34px;
    line-height: 1.05;
  }
  .contact {
    position: absolute;
    left: 44px; bottom: 40px;
  }
  .contact .person-name {
    color: var(--brand-blue);
    font-size: 21px;
  }
  .contact .person-title {
    color: var(--brand-green);
    font-size: 19px;
    margin-bottom: 8px;
  }
  .contact .line {
    display: flex;
    align-items: center;
    gap: 8px;
    color: var(--ink);
    font-size: 21px;
    line-height: 1.3;
  }
  .contact svg { width: 20px; height: 20px; flex: none; }
</style>
</head>
<body>
<main class="stage">
  <section class="card card-back" aria-label="Card back">
    <div class="band-top"></div>
    <div class="back-name">KWT</div>
  </section>

  <section class="card card-front" aria-label="Card front">
    <div class="frame"></div>
    <div class="brand">
      <div class="brand-square"></div>
      <div class="brand-name">Wexmoor<br>Dental Group</div>
    </div>
    <div class="contact">
      <p class="person-name">Lena Marsh</p>
      <p class="person-title">Manager</p>
      <p class="line">
        <svg viewBox="0 0 24 24" aria-hidden="true"><path fill="#14ab4b" d="M6.6 10.8a15.1 15.1 0 0 0 6.6 6.6l2.2-2.2a1 1 0 0 1 1-.25 11.4 11.4 0 0 0 3.6.57 1 1 0 0 1 1 1V20a1 1 0 0 1-1 1A17 17 0 0 1 3 4a1 1 0 0 1 1-1h3.5a1 1 0 0 1 1 1c0 1.25.2 2.45.57 3.57a1 1 0 0 1-.25 1z"/></svg>
        204 771 318
      </p>
      <p class="line">
        <svg viewBox="0 0 24 24" aria-hidden="true"><g fill="none" stroke="#14ab4b" stroke-width="2"><circle cx="12" cy="12" r="9.5"/><ellipse cx="12" cy="12" rx="4" ry="9.5"/><path d="M2.5 12h19M4 7h16M4 17h16"/></g></svg>
        wexmoordental.com
      </p>
    </div>
  </section>
</main>
</body>
</html>
```